Display ads - Med spa Velmira promotion

Please create an ad creative for a promotional special for a med spa:
First-time customers who book a Velmira appointment receive $50 off the Velmira treatment

Please have an aspect of diversity in the ad (the company is black and woman-owned, so more than just white people in the ad creative

The company goes for "clean and tranquil" as part of their aesthetic

Attached here are the logo and picture of the homepage, and other images on the website, typical of the aesthetic of the company identity

you can find the website here for inspiration: thedewlinestudioct.com

Please no "black and white" photography, full color only, thank you!

Target Market(s)

New Haven, Connecticut, wealthy individuals who want to look and feel younger, want great skin, and want to feel youthful

Industry/Entity Type

Medspa/beauty

Requirements
Must have
• Need 5 sizes that fit the following Medium rectangle: 300×250; Large rectangle: 300×600 ; 728x90, 300x50; 160x600
Nice to have
• Clean, refined, bright
Should not have
• black and white photos, cartoonish, or drawn items

```html
<!DOCTYPE html>
<html lang="en">
<head>
<meta charset="utf-8">
<title>The Dewline Studio – Velmira Display Ads</title>
<link rel="stylesheet" href="https://fonts.googleapis.com/css2?family=Oswald:wght@300;400&family=Montserrat:wght@400;500&family=Playfair+Display:ital@1&display=swap">
<style>
  :root {
    --page: #ffffff;
    --green: #4b6349;
    --sand: #d8c2ae;
    --label: #111111;
    --photo-a: #3a2a22;
    --photo-b: #8c6450;
    --photo-c: #c99a7e;
  }
  * { box-sizing: border-box; margin: 0; padding: 0; }
  html, body { width: 1114px; height: 1200px; overflow: hidden; background: var(--page); }
  .canvas { position: relative; width: 1114px; height: 1200px; }

  .size-label {
    position: absolute; font-family: "Montserrat", sans-serif; font-size: 16px;
    color: var(--label); text-align: center; width: 300px;
  }

  .banner { position: absolute; background: var(--green); overflow: hidden; color: var(--sand); }
  .banner .frame { position: absolute; inset: 8px; border: 1.5px solid var(--sand); opacity: .55; z-index: 3; pointer-events: none; }

  .photo {
    position: absolute;
    background:
      radial-gradient(ellipse 30% 55% at 22% 45%, var(--photo-a), transparent 70%),
      radial-gradient(ellipse 28% 55% at 55% 45%, var(--photo-c), transparent 72%),
      radial-gradient(ellipse 28% 55% at 85% 45%, var(--photo-c), transparent 72%),
      linear-gradient(90deg, var(--photo-a), var(--photo-b) 45%, var(--photo-a) 60%, var(--photo-b));
    z-index: 1;
  }

  .brand { position: absolute; display: flex; align-items: center; gap: 12px; z-index: 2; }
  .brand .mark { border-radius: 50%; border: 3px solid var(--sand); flex: none; }
  .brand .name { font-family: "Montserrat", sans-serif; font-weight: 400; line-height: 1.08; color: var(--sand); }

  .headline {
    position: absolute; font-family: "Oswald", sans-serif; font-weight: 300;
    text-align: center; text-transform: uppercase; line-height: 1.18; z-index: 2; letter-spacing: .01em;
  }

  .offer {
    position: absolute; border: 5px solid var(--sand); display: flex; flex-direction: column;
    align-items: center; justify-content: center; text-align: center; z-index: 2;
  }
  .offer .lead, .offer .fine { font-family: "Montserrat", sans-serif; font-weight: 500; text-transform: uppercase; letter-spacing: .04em; }
  .offer .amount { font-family: "Playfair Display", serif; font-style: italic; line-height: .9; }
</style>
</head>
<body>
<main class="canvas">

  <!-- 300 x 600 -->
  <p class="size-label" style="left:80px; top:84px;">banner 300x600px</p>
  <section class="banner" style="left:34px; top:117px; width:393px; height:786px;">
    <div class="frame"></div>
    <div class="brand" style="left:86px; top:42px;">
      <span class="mark" style="width:40px; height:40px;"></span>
      <span class="name" style="font-size:25px;">The<br>Dewline<br>Studio</span>
    </div>
    <h2 class="headline" style="left:0; right:0; top:140px; font-size:41px;">Book a Velmira<br>Appointment</h2>
    <div class="offer" style="left:79px; top:258px; width:232px; height:232px;">
      <span class="lead" style="font-size:13px; margin-bottom:6px;">Receive</span>
      <span class="amount" style="font-size:72px;">$50<br>OFF</span>
      <span class="fine" style="font-size:12px; margin-top:8px;">The Velmira Treatment</span>
    </div>
    <div class="photo" role="img" aria-label="Close-up photo of three women of diverse skin tones with glowing skin" style="left:0; top:453px; width:393px; height:333px;"></div>
  </section>

  <!-- 160 x 600 -->
  <p class="size-label" style="left:401px; top:84px;">banner 160x600px</p>
  <section class="banner" style="left:447px; top:117px; width:208px; height:786px;">
    <div class="frame"></div>
    <div class="brand" style="left:20px; top:34px; gap:10px;">
      <span class="mark" style="width:34px; height:34px;"></span>
      <span class="name" style="font-size:20px;">The<br>Dewline<br>Studio</span>
    </div>
    <h2 class="headline" style="left:0; right:0; top:122px; font-size:40px; line-height:1.15;">Book<br>a Velmira<br>Appoint-<br>ment</h2>
    <div class="offer" style="left:17px; top:331px; width:174px; height:174px; border-width:4px;">
      <span class="lead" style="font-size:11px; margin-bottom:4px;">Receive</span>
      <span class="amount" style="font-size:54px;">$50<br>OFF</span>
      <span class="fine" style="font-size:9px; margin-top:6px;">The Velmira Treatment</span>
    </div>
    <div class="photo" role="img" aria-label="Photo of two women of diverse skin tones with glowing skin" style="left:0; top:525px; width:208px; height:261px;"></div>
  </section>

  <!-- 300 x 50 -->
  <p class="size-label" style="left:722px; top:412px;">banner 300x50px</p>
  <section class="banner" style="left:676px; top:446px; width:393px; height:63px;">
    <div class="frame" style="inset:3px; border-width:1px;"></div>
    <div class="photo" role="img" aria-label="Photo of three women of diverse skin tones" style="left:0; top:0; width:164px; height:63px;"></div>
    <h2 class="headline" style="left:166px; top:6px; width:56px; font-size:10px; line-height:1.2; text-align:left;">Book a<br>Velmira<br>Appoint-<br>ment</h2>
    <div class="offer" style="left:224px; top:6px; width:50px; height:51px; border-width:2px;">
      <span class="lead" style="font-size:4px;">Receive</span>
      <span class="amount" style="font-size:16px;">$50<br>OFF</span>
      <span class="fine" style="font-size:3px; margin-top:1px;">The Velmira Treatment</span>
    </div>
    <div class="brand" style="left:284px; top:11px; gap:6px;">
      <span class="mark" style="width:16px; height:16px; border-width:2px;"></span>
      <span class="name" style="font-size:11px;">The<br>Dewline<br>Studio</span>
    </div>
  </section>

  <!-- 300 x 250 -->
  <p class="size-label" style="left:722px; top:543px;">banner 300x250px</p>
  <section class="banner" style="left:676px; top:575px; width:393px; height:328px;">
    <div class="frame"></div>
    <div class="brand" style="left:30px; top:24px;">
      <span class="mark" style="width:40px; height:40px;"></span>
      <span class="name" style="font-size:25px;">The<br>Dewline<br>Studio</span>
    </div>
    <div class="offer" style="left:282px; top:21px; width:87px; height:87px; border-width:3px;">
      <span class="lead" style="font-size:6px;">Receive</span>
      <span class="amount" style="font-size:28px;">$50<br>OFF</span>
      <span class="fine" style="font-size:5px; margin-top:3px;">The Velmira Treatment</span>
    </div>
    <h2 class="headline" style="left:0; right:0; top:123px; font-size:30px;">Book a Velmira Appointment</h2>
    <div class="photo" role="img" aria-label="Photo of three women of diverse skin tones with glowing skin" style="left:0; top:165px; width:393px; height:163px;"></div>
  </section>

  <!-- 728 x 90 -->
  <p class="size-label" style="left:387px; top:950px;">banner 728x90px</p>
  <section class="banner" style="left:60px; top:983px; width:954px; height:118px;">
    <div class="frame"></div>
    <div class="photo" role="img" aria-label="Photo of three women of diverse skin tones with glowing skin" style="left:0; top:0; width:280px; height:118px;"></div>
    <h2 class="headline" style="left:300px; width:266px; top:9px; font-size:38px; line-height:1.25;">Book a Velmira<br>Appointment</h2>
    <div class="offer" style="left:583px; top:9px; width:96px; height:98px; border-width:3px;">
      <span class="lead" style="font-size:7px;">Receive</span>
      <span class="amount" style="font-size:31px;">$50<br>OFF</span>
      <span class="fine" style="font-size:5px; margin-top:3px;">The Velmira Treatment</span>
    </div>
    <div class="brand" style="left:706px; top:22px;">
      <span class="mark" style="width:40px; height:40px;"></span>
      <span class="name" style="font-size:25px;">The<br>Dewline<br>Studio</span>
    </div>
  </section>

</main>
</body>
</html>
```